Technology solutions catalog

Were looking for a catalogue to supplement our website and corporate branding.

Our website will give you a good understanding of our products and services as well as our theme.

Our base colour and logo is red, white and grey.

www.voltrane.com.au

The aim of the catalogue is to showcase our business IT services & solutions. This will be a mix of education about the new solutions available to small and medium business today and how these solutions can increase productivity.

We would also like tip sections

This isn't all about selling but also about educating SMB's of the new and exciting IT solutions available today and having them book a free consult with us to discuss further about how we can help the business.

Solutions and area's that the catalogue will need to cover include

Front Cover -
-About us section, with our business contact information (1st page)
- Introduction. (2nd page)
-Communication Solutions - this includes Email, IP phones and business IT networks (2 pages)
- Data & Storage solutions (2 pages)
- Hardware (1 pages)
- Business IT health check list (1 page)
- Services and support offering (2 pages)
- Software & Popular cloud solutions (2 pages)
- Website / E-commerce solutions (2 pages)
Back cover

Based on two pages per solution the whole catalogue will be around 14 pages.

We don't need any text content done. We would like Headings on pages including page numbers. Footer please.

We're looking for a template that we can have our designer finish off by adding in some further product and service image and text.

Thank you for your consideration

Target Market(s)

IT for small and medium businesses

Industry/Entity Type

Supplement

Requirements
Must have
• Size A4
• Design supplied in Adobe indesign so we can edit and add our text and content
• Clean design

```html
<!DOCTYPE html>
<html lang="en">
<head>
<meta charset="utf-8">
<title>Voltrane Catalogue Cover</title>
<link href="https://fonts.googleapis.com/css2?family=Open+Sans:wght@400;700;800&display=swap" rel="stylesheet">
<style>
  :root {
    --stage: #8f8f8f;
    --red: #e52630;
    --red-deep: #b81d26;
    --charcoal: #1f1f1f;
    --charcoal-soft: #2e2e2e;
    --silver: #d9d9d9;
    --paper: #ffffff;
    --text-light: #e8e8e8;
  }
  html, body {
    margin: 0;
    width: 1200px;
    height: 900px;
    overflow: hidden;
    background: var(--stage);
  }
  .cover {
    position: absolute;
    left: 40px;
    top: 54px;
    width: 1120px;
    height: 792px;
    background: var(--paper);
    box-shadow: 0 10px 30px rgba(0,0,0,0.25);
  }
  .cover-art {
    position: absolute;
    inset: 0;
    display: block;
  }
  .brand {
    position: absolute;
    left: 100px;
    top: 628px;
    font-family: "Open Sans", Arial, sans-serif;
    color: var(--text-light);
  }
  .brand-name {
    margin: 0;
    font-size: 60px;
    font-weight: 800;
    line-height: 1;
    letter-spacing: 0.5px;
  }
  .brand-url {
    margin: 12px 0 0 4px;
    font-size: 12px;
    font-weight: 400;
    color: var(--text-light);
  }
</style>
</head>
<body>
  <div class="cover">
    <svg class="cover-art" viewBox="0 0 1120 792" xmlns="http://www.w3.org/2000/svg">
      <defs>
        <linearGradient id="redPanel" x1="0" y1="0" x2="1" y2="0.4">
          <stop offset="0" stop-color="var(--red-deep)"/>
          <stop offset="1" stop-color="var(--red)"/>
        </linearGradient>
        <linearGradient id="darkPanel" x1="0" y1="0" x2="1" y2="1">
          <stop offset="0" stop-color="var(--charcoal-soft)"/>
          <stop offset="1" stop-color="var(--charcoal)"/>
        </linearGradient>
        <linearGradient id="photoTone" x1="0" y1="0" x2="1" y2="1">
          <stop offset="0" stop-color="#f7f9fb"/>
          <stop offset="0.45" stop-color="#d9e2ea"/>
          <stop offset="1" stop-color="#b9a99a"/>
        </linearGradient>
      </defs>

      <polygon class="photo-area" role="img"
        aria-label="Photo of two colleagues planning with colourful sticky notes on a glass wall"
        points="526,0 1120,0 1120,792 717,792 280,454"
        fill="url(#photoTone)"/>

      <polygon class="silver-edge" points="516,0 532,0 288,450 276,452" fill="var(--silver)"/>
      <polygon class="red-panel" points="0,0 514,0 274,452 0,238" fill="url(#redPanel)"/>

      <polygon class="silver-edge" points="0,232 726,792 706,792 0,246" fill="var(--silver)"/>
      <polygon class="dark-panel" points="0,244 704,792 0,792" fill="url(#darkPanel)"/>
    </svg>

    <div class="brand">
      <p class="brand-name">Voltrane</p>
      <p class="brand-url">www.voltrane.com.au</p>
    </div>
  </div>
</body>
</html>
```